Harrowgate Automotive Business Card

Automotive repair , all makes including Asian and European Imports. TQR Certified (Logo),fennlo (logo), Qwindle+ (logo)

Industry/Entity Type

Automotive

Contact Information for Business Card

Harrowgate Automotive, Carl Obrenski Owner, 3826 Poplar Rd. Worthington, Mn 56187. Website harrowgateautomotive.com. (612) 555-0148

```html
<!DOCTYPE html>
<html lang="en">
<head>
<meta charset="utf-8">
<title>Harrowgate Automotive Business Card</title>
<link rel="stylesheet" href="https://fonts.googleapis.com/css2?family=Open+Sans:wght@400;600;700;800&display=swap">
<style>
  :root {
    --brand-blue: #2449a6;
    --brand-red: #c0232b;
    --ink-grey: #6d6d6d;
    --paper: #ffffff;
    --backdrop: #e7e8ea;
  }
  * { margin: 0; padding: 0; box-sizing: border-box; }
  html, body { width: 1200px; height: 900px; overflow: hidden; }
  body {
    background: var(--backdrop);
    font-family: "Open Sans", Arial, sans-serif;
    display: flex;
    flex-direction: column;
    align-items: center;
    justify-content: center;
    gap: 40px;
  }
  .card {
    position: relative;
    width: 700px;
    height: 400px;
    overflow: hidden;
    box-shadow: 0 6px 18px rgba(0,0,0,0.18);
  }
  /* Front side */
  .card-front {
    background: var(--brand-blue);
    display: flex;
    align-items: center;
    justify-content: center;
    gap: 22px;
  }
  .front-mark {
    width: 56px; height: 56px;
    border-radius: 50%;
    background: var(--paper);
  }
  .front-name {
    color: var(--paper);
    font-weight: 800;
    font-size: 50px;
    line-height: 1.05;
  }
  /* Back side */
  .card-back { background: var(--paper); }
  .card-back .waves { position: absolute; inset: 0; }
  .back-logo {
    position: absolute;
    left: 40px; top: 38px;
    display: flex; align-items: center; gap: 12px;
  }
  .back-logo .mark {
    width: 26px; height: 26px;
    background: var(--brand-red);
  }
  .back-logo .name {
    color: var(--brand-blue);
    font-weight: 800;
    font-size: 30px;
  }
  .holder {
    position: absolute;
    left: 40px; top: 168px;
  }
  .holder-name {
    color: var(--brand-red);
    font-weight: 700;
    font-size: 28px;
    line-height: 1.1;
  }
  .holder-title {
    color: var(--ink-grey);
    font-size: 16px;
    font-weight: 600;
    margin-top: 2px;
  }
  .contact {
    position: absolute;
    right: 24px; top: 212px;
    color: var(--paper);
    text-align: right;
    font-size: 15px;
    font-weight: 600;
    line-height: 1.45;
  }
  .address { margin-bottom: 8px; }
  .contact-line {
    display: flex; justify-content: flex-end; align-items: center; gap: 10px;
    font-size: 15px;
    line-height: 1.45;
  }
  .contact-line svg { width: 13px; height: 13px; flex: none; }
</style>
</head>
<body>

<section class="card card-front" aria-label="Card front">
  <span class="front-mark" aria-hidden="true"></span>
  <h1 class="front-name">Harrowgate<br>Automotive</h1>
</section>

<section class="card card-back" aria-label="Card back">
  <svg class="waves" viewBox="0 0 700 400" aria-hidden="true">
    <path d="M0,240 C220,262 420,160 700,95 L700,115 C420,182 220,284 0,262 Z" fill="var(--brand-blue)"/>
    <path d="M0,275 C220,300 420,190 700,130 L700,400 L0,400 Z" fill="var(--brand-red)"/>
    <path d="M0,335 C180,350 330,318 440,288" fill="none" stroke="var(--paper)" stroke-width="4" stroke-linecap="round"/>
    <path d="M0,365 C120,380 220,392 300,400 L0,400 Z" fill="var(--paper)"/>
  </svg>

  <div class="back-logo">
    <span class="mark" aria-hidden="true"></span>
    <span class="name">Harrowgate Automotive</span>
  </div>

  <div class="holder">
    <p class="holder-name">Carl Obrenski</p>
    <p class="holder-title">Managing Member</p>
  </div>

  <div class="contact">
    <p class="address">3826 Poplar Rd.,<br>Worthington, MN 56187</p>
    <p class="contact-line">(612) 555-0148
      <svg viewBox="0 0 16 16"><path d="M4 1l3 3-2 2c1 2 3 4 5 5l2-2 3 3-2 3C7 15 1 9 1 3z" fill="#fff"/></svg></p>
    <p class="contact-line">(612) 555-0149
      <svg viewBox="0 0 16 16"><rect x="4" y="1" width="8" height="5" fill="#fff"/><rect x="1" y="6" width="14" height="7" rx="1" fill="#fff"/></svg></p>
    <p class="contact-line">(612) 555-0172
      <svg viewBox="0 0 16 16"><rect x="4" y="1" width="8" height="14" rx="1.5" fill="none" stroke="#fff" stroke-width="1.6"/></svg></p>
    <p class="contact-line">carl@harrowgateauto.com
      <svg viewBox="0 0 16 16"><rect x="1" y="3" width="14" height="10" fill="#fff"/><path d="M1 3l7 6 7-6" fill="none" stroke="#c0232b" stroke-width="1.3"/></svg></p>
    <p class="contact-line">www.harrowgateautomotive.com
      <svg viewBox="0 0 16 16"><circle cx="8" cy="8" r="6.5" fill="none" stroke="#fff" stroke-width="1.5"/><path d="M1.5 8h13M8 1.5c-3 3-3 10 0 13M8 1.5c3 3 3 10 0 13" fill="none" stroke="#fff" stroke-width="1.2"/></svg></p>
  </div>
</section>

</body>
</html>
```